Online hair business needs a Glam Web and Logo design*

I am launching an online business selling Brazillian Hair Weave. My business name is ZolaT Tresses and I would love a logo with a glamorous female image, maybe a silhouette, with long wavy hair and I would like the initials ZTT or ZT somewhere in the logo on the top, bottom or as jewelry (earrings/necklace). It does not have to be a female image, but it needs to be eye-catching.

Industry/Entity Type

Hair And Beauty

Logo Text

ZolaT Tresses

Number of Pages Required

1 page

Font styles to use
Sans Serif

Colors

Designer to choose colors to be used in the design.

Requirements
Nice to have
• I need to display the hair to sell, but would also like to display models or images with the hair installed. I also need to have FAQ's and would like to be able to add some videos.

```html
<!DOCTYPE html>
<html lang="en">
<head>
<meta charset="utf-8">
<title>ZolaT Tresses</title>
<link href="https://fonts.googleapis.com/css2?family=Open+Sans:wght@400;600;700&family=Oswald:wght@500;700&family=Oleo+Script:wght@700&display=swap" rel="stylesheet">
<style>
:root{
  --orange:#f26a10;
  --orange-dark:#d8540a;
  --ink:#333333;
  --muted:#8a8a8a;
  --line:#e2e2e2;
  --grey-bg:#ececec;
  --footer:#1f1f1f;
  --footer-deep:#161616;
  --white:#ffffff;
}
*{margin:0;padding:0;box-sizing:border-box}
html,body{width:1200px;height:3060px;overflow:hidden}
body{font-family:"Open Sans",sans-serif;color:var(--ink);background:var(--white);position:relative}

/* header */
.site-header{position:absolute;top:0;left:0;width:1200px;height:104px;background:var(--white)}
.brand{position:absolute;left:40px;top:24px;display:flex;align-items:center;gap:10px}
.brand-dot{width:56px;height:56px;border-radius:50%;background:var(--orange)}
.brand-name{font-weight:700;font-size:30px;color:var(--orange)}
.main-nav{position:absolute;right:40px;top:0;height:104px;display:flex;align-items:center;gap:40px;font-size:16px}
.main-nav a{color:#555;text-decoration:none}
.main-nav a.active{color:var(--orange)}
.cart{display:flex;align-items:center;gap:8px;color:#555}

/* hero */
.hero{position:absolute;top:104px;left:0;width:1200px;height:536px;background:linear-gradient(90deg,#0e0e0e 0%,#1a1716 38%,#2a1610 52%,#5a220a 100%);overflow:hidden}
.hero-photo{position:absolute;right:0;top:0;width:720px;height:536px;background:
  radial-gradient(ellipse 38% 55% at 78% 35%,#f4d6c4 0%,#e8a47c 18%,rgba(232,120,60,0) 40%),
  radial-gradient(ellipse 70% 80% at 55% 55%,#ff7a2a 0%,#e6521a 30%,#a8300c 58%,rgba(40,18,12,0) 100%)}
.hero-title{position:absolute;left:88px;top:232px;font-family:"Oleo Script",sans-serif;font-weight:700;font-size:58px;color:var(--white)}
.hero-sub{position:absolute;left:88px;top:312px;font-family:"Oswald",sans-serif;font-weight:500;font-size:26px;color:var(--white)}
.btn-outline{position:absolute;left:88px;top:362px;width:130px;height:38px;border:2px solid var(--white);border-radius:19px;color:var(--white);font-size:14px;display:flex;align-items:center;justify-content:center;letter-spacing:.5px}
.hero-arrows{position:absolute;left:100px;top:460px;display:flex;gap:24px}

/* welcome */
.welcome-media{position:absolute;left:88px;top:740px;width:440px;height:292px;background:
  radial-gradient(ellipse 40% 60% at 45% 45%,#e9cdb4 0%,#c49468 40%,rgba(180,130,90,0) 75%),
  linear-gradient(135deg,#8a5a34,#c9a27c 45%,#efe7de 100%)}
.play{position:absolute;left:190px;top:116px}
.welcome-title{position:absolute;left:544px;top:760px;font-family:"Oleo Script",sans-serif;font-weight:700;font-size:34px;color:#222}
.welcome-title span{color:var(--orange)}
.welcome-text{position:absolute;left:544px;top:816px;width:600px;font-size:13px;line-height:22px;color:var(--muted)}
.btn-solid{position:absolute;left:544px;top:982px;width:110px;height:30px;border-radius:15px;background:var(--orange);color:var(--white);font-size:12px;display:flex;align-items:center;justify-content:center}

/* products */
.products-band{position:absolute;top:1120px;left:0;width:1200px;height:300px;background:linear-gradient(180deg,var(--orange-dark),var(--orange))}
.section-title{font-family:"Oleo Script",sans-serif;font-weight:700;font-size:36px;text-align:center;width:1200px;position:absolute;left:0}
.products-title{top:1164px;color:var(--white)}
.product-card{position:absolute;top:1260px;width:228px;height:272px;background:var(--white);box-shadow:0 4px 12px rgba(0,0,0,.18);border-bottom:5px solid var(--orange)}
.product-img{position:absolute;left:14px;top:14px;width:200px;height:200px;background-color:#fff}
.product-name{position:absolute;left:0;top:228px;width:228px;text-align:center;font-size:15px;color:#444}

/* faq */
.faq{position:absolute;top:1640px;left:0;width:1200px;height:600px;background:var(--grey-bg)}
.faq-title{top:1704px;color:#222}
.faq-item{position:absolute;width:464px;background:var(--white);border:1px solid var(--line);box-shadow:0 1px 3px rgba(0,0,0,.08);padding:12px 14px;font-size:12px;color:#444}
.faq-q{display:flex;gap:8px;align-items:center}
.faq-a{display:flex;gap:8px;margin-top:8px;color:var(--muted);font-size:11px;line-height:17px}
.ic{flex:none}

/* blog */
.blog-title{top:2330px;color:#222}
.post{position:absolute;top:2428px;width:200px}
.post-img{width:200px;height:136px}
.post-text{margin-top:14px;font-size:12px;line-height:18px;color:#555}
.post-date{margin-top:10px;font-size:11px;color:var(--orange);display:flex;align-items:center;gap:6px}

/* footer */
.site-footer{position:absolute;top:2720px;left:0;width:1200px;height:340px;background:var(--footer);color:#cfcfcf}
.f-col{position:absolute;top:40px;font-size:12px;line-height:22px}
.f-col h4{font-size:13px;font-weight:600;color:var(--white);margin-bottom:12px;letter-spacing:.5px}
.f-list li{list-style:none;display:flex;align-items:center;gap:8px}
.f-list li::before{content:"";width:4px;height:4px;background:var(--orange);border-radius:50%}
.f-row{display:flex;align-items:center;gap:8px}
.subscribe{display:flex;margin-top:8px}
.subscribe .field{width:150px;height:28px;background:var(--white);color:#999;font-size:10px;padding:6px 8px}
.subscribe .go{width:64px;height:28px;background:var(--orange);color:var(--white);font-size:11px;display:flex;align-items:center;justify-content:center}
.social{display:flex;gap:12px;margin-top:4px}
.social span{width:28px;height:28px;border-radius:4px;background:#d8d8d8}
.copyright{position:absolute;left:0;bottom:0;width:1200px;height:60px;background:var(--footer-deep);color:#9a9a9a;font-size:11px;display:flex;align-items:center;justify-content:center}
</style>
</head>
<body>

<header class="site-header">
  <div class="brand"><span class="brand-dot"></span><span class="brand-name">ZTT</span></div>
  <nav class="main-nav">
    <a class="active" href="#">Home</a>
    <a href="#">About us</a>
    <a href="#">Products</a>
    <a href="#">Shop</a>
    <a href="#">Blog</a>
    <a href="#">Contact</a>
    <span class="cart">
      <svg width="18" height="16" viewBox="0 0 18 16"><path d="M1 1h3l2 9h9l2-6H5" fill="none" stroke="#555" stroke-width="1.6"/><circle cx="7" cy="14" r="1.5" fill="#555"/><circle cx="14" cy="14" r="1.5" fill="#555"/></svg>
      0
    </span>
  </nav>
</header>

<section class="hero">
  <div class="hero-photo" role="img" aria-label="Model with long voluminous copper-red wavy hair"></div>
  <h1 class="hero-title">ZolaT Tresses</h1>
  <p class="hero-sub">Neque porro quisquam qui dolorem</p>
  <span class="btn-outline">VIEW MORE</span>
  <div class="hero-arrows">
    <svg width="10" height="14" viewBox="0 0 10 14"><path d="M8 1L2 7l6 6" fill="none" stroke="#fff" stroke-width="2"/></svg>
    <svg width="10" height="14" viewBox="0 0 10 14"><path d="M2 1l6 6-6 6" fill="none" stroke="#fff" stroke-width="2"/></svg>
  </div>
</section>

<section>
  <div class="welcome-media" role="img" aria-label="Video still of a smiling model with long honey-blonde waves">
    <svg class="play" width="60" height="60" viewBox="0 0 60 60"><circle cx="30" cy="30" r="28" fill="rgba(0,0,0,.35)"/><path d="M24 18l18 12-18 12z" fill="#fff"/></svg>
  </div>
  <h2 class="welcome-title">Welcome to <span>ZolaT Tresses</span></h2>
  <p class="welcome-text">The point of using Lorem Ipsum is that it has a more-or-less normal distribution of letters, as opposed to using 'Content here, content here', making it look like readable English. Many desktop publishing packages and web page editors now use Lorem Ipsum as their default model text, and a search for 'lorem ipsum' will uncover many web sites still in their infancy. Various versions have evolved over the years, sometimes by accident.</p>
  <span class="btn-solid">Read More</span>
</section>

<section>
  <div class="products-band"></div>
  <h2 class="section-title products-title">Our Products</h2>
  <div class="product-card" style="left:100px"><div class="product-img" role="img" aria-label="Ombre body wave hair bundle, dark roots to honey blonde ends" style="background-image:radial-gradient(ellipse 24% 48% at 50% 50%,#a8773f 0%,#6a4526 45%,#2a1c14 70%,rgba(255,255,255,0) 100%)"></div><p class="product-name">Product Name</p></div>
  <div class="product-card" style="left:356px"><div class="product-img" role="img" aria-label="Natural black body wave hair bundle" style="background-image:radial-gradient(ellipse 26% 46% at 50% 50%,#2a2624 0%,#1a1716 55%,rgba(255,255,255,0) 100%)"></div><p class="product-name">Product Name</p></div>
  <div class="product-card" style="left:620px"><div class="product-img" role="img" aria-label="Natural black loose wave hair bundle" style="background-image:radial-gradient(ellipse 24% 46% at 50% 50%,#302a27 0%,#1c1918 55%,rgba(255,255,255,0) 100%)"></div><p class="product-name">Product Name</p></div>
  <div class="product-card" style="left:876px"><div class="product-img" role="img" aria-label="Natural black deep wave hair bundle" style="background-image:radial-gradient(ellipse 26% 44% at 50% 50%,#2c2725 0%,#181514 55%,rgba(255,255,255,0) 100%)"></div><p class="product-name">Product Name</p></div>
</section>

<section class="faq"></section>
<h2 class="section-title faq-title">FAQ</h2>

<div class="faq-item" style="left:108px;top:1800px">
  <div class="faq-q"><svg class="ic" width="12" height="12" viewBox="0 0 12 12"><circle cx="6" cy="6" r="5" fill="none" stroke="#555"/><path d="M4.5 4.5a1.5 1.5 0 1 1 1.5 1.5v1" fill="none" stroke="#555"/></svg>Neque porro quisquam est qui dolorem ipsum quia dolor ?</div>
  <div class="faq-a"><svg class="ic" width="12" height="12" viewBox="0 0 12 12"><circle cx="6" cy="6" r="5" fill="var(--orange)"/></svg>It is a long established fact that a reader will be distracted by the readable content of a page when looking at its layout. The point of using Lorem.</div>
</div>
<div class="faq-item" style="left:108px;top:1906px"><div class="faq-q"><svg class="ic" width="12" height="12" viewBox="0 0 12 12"><circle cx="6" cy="6" r="5" fill="none" stroke="#555"/></svg>Quisquam est qui dolorem ipsum quia dolor sit amet ?</div></div>
<div class="faq-item" style="left:108px;top:1962px"><div class="faq-q"><svg class="ic" width="12" height="12" viewBox="0 0 12 12"><circle cx="6" cy="6" r="5" fill="none" stroke="#555"/></svg>Neque porro quisquam est qui dolorem ipsum quia dolor ?</div></div>
<div class="faq-item" style="left:108px;top:2018px"><div class="faq-q"><svg class="ic" width="12" height="12" viewBox="0 0 12 12"><circle cx="6" cy="6" r="5" fill="none" stroke="#555"/></svg>Porro quisquam est qui dolorem ipsum quia dolor sit amet ?</div></div>

<div class="faq-item" style="left:620px;top:1800px"><div class="faq-q"><svg class="ic" width="12" height="12" viewBox="0 0 12 12"><circle cx="6" cy="6" r="5" fill="none" stroke="#555"/></svg>Quisquam porro qui dolorem ipsum quia dolor sit amet ?</div></div>
<div class="faq-item" style="left:620px;top:1856px"><div class="faq-q"><svg class="ic" width="12" height="12" viewBox="0 0 12 12"><circle cx="6" cy="6" r="5" fill="none" stroke="#555"/></svg>Neque porro quisquam est qui dolorem ipsum quia dolor ?</div></div>
<div class="faq-item" style="left:620px;top:1912px"><div class="faq-q"><svg class="ic" width="12" height="12" viewBox="0 0 12 12"><circle cx="6" cy="6" r="5" fill="none" stroke="#555"/></svg>Porro quisquam est qui dolorem ipsum quia dolor sit amet ?</div></div>
<div class="faq-item" style="left:620px;top:1968px">
  <div class="faq-q"><svg class="ic" width="12" height="12" viewBox="0 0 12 12"><circle cx="6" cy="6" r="5" fill="none" stroke="#555"/></svg>Neque porro quisquam est qui dolorem ipsum quia dolor ?</div>
  <div class="faq-a"><svg class="ic" width="12" height="12" viewBox="0 0 12 12"><circle cx="6" cy="6" r="5" fill="var(--orange)"/></svg>It is a long established fact that a reader will be distracted by the readable content of a page when looking at its layout. The point of using Lorem.</div>
</div>

<h2 class="section-title blog-title">Latest Blog</h2>
<article class="post" style="left:132px"><div class="post-img" role="img" aria-label="Model with long caramel waves" style="background:radial-gradient(ellipse 60% 80% at 40% 50%,#b98456 0%,#8a5a36 45%,#e9ddd0 100%)"></div><p class="post-text">It has survived not only five centuries but also the leap</p><p class="post-date"><svg width="11" height="11" viewBox="0 0 11 11"><rect x="1" y="2" width="9" height="8" fill="none" stroke="var(--orange)"/></svg>10 March, 2016</p></article>
<article class="post" style="left:380px"><div class="post-img" role="img" aria-label="Model with dark brown curly hair" style="background:radial-gradient(ellipse 60% 80% at 55% 50%,#4a2e1e 0%,#6e4a32 45%,#e2d8cc 100%)"></div><p class="post-text">It has survived not only five centuries but also the leap</p><p class="post-date"><svg width="11" height="11" viewBox="0 0 11 11"><rect x="1" y="2" width="9" height="8" fill="none" stroke="var(--orange)"/></svg>7 March, 2016</p></article>
<article class="post" style="left:628px"><div class="post-img" role="img" aria-label="Model with copper brown wavy hair" style="background:radial-gradient(ellipse 60% 80% at 50% 50%,#b5622c 0%,#7a3a18 45%,#2a1a12 100%)"></div><p class="post-text">It has survived not only five centuries but also the leap</p><p class="post-date"><svg width="11" height="11" viewBox="0 0 11 11"><rect x="1" y="2" width="9" height="8" fill="none" stroke="var(--orange)"/></svg>3 January, 2016</p></article>
<article class="post" style="left:880px"><div class="post-img" role="img" aria-label="Model with blonde wavy hair" style="background:radial-gradient(ellipse 60% 80% at 50% 50%,#d8b88a 0%,#c49e6c 45%,#f1ebe2 100%)"></div><p class="post-text">It has survived not only five centuries but also the leap</p><p class="post-date"><svg width="11" height="11" viewBox="0 0 11 11"><rect x="1" y="2" width="9" height="8" fill="none" stroke="var(--orange)"/></svg>7 January, 2016</p></article>

<footer class="site-footer">
  <div class="f-col" style="left:88px">
    <h4>INFORMATION</h4>
    <ul class="f-list"><li>Privacy Policy</li><li>Your Account</li><li>Advanced Search</li><li>Contact Us</li></ul>
  </div>
  <div class="f-col" style="left:336px">
    <h4>CONTACT US</h4>
    <div class="f-row"><svg width="10" height="12" viewBox="0 0 10 12"><path d="M5 11S1 7 1 4.5a4 4 0 0 1 8 0C9 7 5 11 5 11z" fill="var(--orange)"/></svg>418 Amberline Avenue</div>
    <div class="f-row"><svg width="10" height="10" viewBox="0 0 10 10"><path d="M2 1l2 2-1 1.5a6 6 0 0 0 2.5 2.5L7 6l2 2-1.5 1.5C4 9 1 6 .5 2.5z" fill="var(--orange)"/></svg>(555) 014-2290</div>
    <div class="f-row"><svg width="10" height="10" viewBox="0 0 10 10"><path d="M2 1l2 2-1 1.5a6 6 0 0 0 2.5 2.5L7 6l2 2-1.5 1.5C4 9 1 6 .5 2.5z" fill="var(--orange)"/></svg>(555) 014-2291</div>
    <div class="f-row"><svg width="11" height="9" viewBox="0 0 11 9"><rect x=".5" y=".5" width="10" height="8" fill="none" stroke="var(--orange)"/><path d="M.5.5l5 4 5-4" fill="none" stroke="var(--orange)"/></svg>hello@zolattresses.com</div>
  </div>
  <div class="f-col" style="left:636px">
    <h4>JOIN OUR MAILING LIST</h4>
    <p>Your latest news and offers delivered to your inbox.</p>
    <div class="subscribe"><span class="field">Email Address</span><span class="go">Submit</span></div>
  </div>
  <div class="f-col" style="left:946px">
    <h4>FOLLOW US OUT THERE</h4>
    <div class="social"><span></span><span></span><span></span><span></span></div>
  </div>
  <div class="copyright">Copyright © 2016 All Rights Reserved</div>
</footer>

</body>
</html>
```